Digital Marketing Online Shop Needs a Home Page Web Design

Here is some background on the new home page and the message we want to relay to people visiting our site.
The new site design will be very similar to the following sites
http://plivora.com/
https://quillmarsh.com/
http://barelytidy.io/
http://craftturnip.com/
http://clipmelon.com/
We are a small marketing agency of 3 and we have built up and impressive contact list of partners over the last 16 years to help our customers take their digital marketing to the next level.
The four core areas of products we will be promoting and selling through our online shop are the following :
Web design
Content marketing
Graphic design
Coaching
We operate our agency in a new way, not the old school way so our customers can receive on-demand marketing.
We plan to have an online shop so visitors can purchase some of our services, very similar to how Quill Marshing and Craft Turnip offer their services.
In the end, we want the same call to action layout as Plivora, Quill Marsh and Craft Turnip, however, since we are an agency we would like to blend in Barely Tidy's layout.
We want the customer to either contact us about our services or purchase one of the services from our shop.
We are trying to make the whole digital marketing experience more transactional like retail and not so traditional servicey. :-)
It is from our years of experience and finding the right partners that allows us to offer this type of solution to businesses in the Maritime Provinces (New Brunswick, Nova Scotia, Prince Edward Island, Canada).
Also, because we are offering more of an on-demand/self serve option and we have lower overhead, we hope to pass along great pricing to our customers for their marketing needs. We really want this offer to expand outside of our local market in Saint John, New Brunswick.
I would also like to have a call to action written for a hero image at the top of the page, like the Plivora site.
After that I would like the content to flow through similar to Quill Marsh & Plivora. But mix in some of the agency like content you see with Clipmelon, Barely Tidy.
I have also included the first draft of the content for our home page.
Menu Items will be About, How We Work, Learn, Shop, Contact
Please let me know if you need anything else.
Small businesses, 1-10 person companies with up to 5 million in revenue. Mostly service companies, but some retail.
Marketing
1 page

```html
<!DOCTYPE html>
<html lang="en">
<head>
<meta charset="utf-8">
<title>Rising Harbour – Digital Marketing for Small Business</title>
<link href="https://fonts.googleapis.com/css2?family=Montserrat:wght@400;600;700;800&family=Lato:wght@400;700&display=swap" rel="stylesheet">
<style>
:root{
  --ink:#2b2d31;
  --muted:#5b5e63;
  --white:#ffffff;
  --accent:#1f6fc0;
  --hero-a:#2f6fb8;
  --hero-b:#5a9ad8;
  --orange:#f0613a;
  --blue:#1aa5e0;
  --yellow:#fbbd2a;
  --teal:#7fbfae;
  --cta-a:#4a4a4c;
  --cta-b:#6b6b6d;
  --footer:#2a2d33;
  --footer-bar:#24272c;
  --footer-text:#c9ccd1;
}
*{box-sizing:border-box;margin:0;padding:0}
html,body{width:1200px;height:4932px;overflow:hidden}
body{font-family:'Lato',sans-serif;color:var(--ink);background:var(--white)}
a{color:inherit;text-decoration:none}

/* Navigation */
.site-nav{height:88px;display:flex;align-items:center;justify-content:space-between;padding:0 48px}
.brand{display:flex;flex-direction:column}
.brand-name{font-family:'Montserrat',sans-serif;font-weight:700;font-size:30px;color:var(--ink);line-height:1}
.brand-tag{font-family:'Montserrat',sans-serif;font-size:10px;letter-spacing:1.5px;color:var(--muted);margin-top:6px}
.nav-links{display:flex;align-items:center;gap:46px;font-family:'Montserrat',sans-serif;font-size:17px;font-weight:600;color:var(--ink)}
.nav-signin{border:2px solid var(--accent);color:var(--accent);border-radius:30px;padding:8px 26px;margin-left:-12px}

/* Hero */
.hero{position:relative;height:655px;color:var(--white);text-align:center}
.hero-bg{position:absolute;inset:0;background:linear-gradient(135deg,var(--hero-a),var(--hero-b) 60%,var(--hero-a))}
.hero-inner{position:relative;padding-top:140px}
.hero-title{font-family:'Montserrat',sans-serif;font-weight:800;font-size:48px;letter-spacing:5px;line-height:1.12;text-transform:uppercase}
.hero-sub{font-family:'Montserrat',sans-serif;font-size:16px;letter-spacing:1px;margin:44px auto 0;width:700px;line-height:1.4}
.btn-row{display:flex;justify-content:center;gap:26px;margin-top:52px}
.btn{display:inline-block;font-family:'Montserrat',sans-serif;font-weight:700;font-size:15px;letter-spacing:1.5px;text-transform:uppercase;padding:14px 44px;border-radius:40px}
.btn-ghost{border:2px solid var(--white);color:var(--white)}
.btn-solid{background:var(--white);color:var(--ink)}

/* Experts */
.experts{height:1026px;text-align:center;padding-top:78px}
.section-title{font-family:'Montserrat',sans-serif;font-weight:600;font-size:32px;color:var(--ink)}
.experts-intro{font-size:16px;line-height:1.9;color:var(--muted);margin:28px auto 0;width:760px}
.team{position:relative;height:720px;margin-top:30px}
.member{position:absolute;top:0;transform:translateX(-50%);text-align:center}
.member-photo{border-radius:50%;margin:0 auto}
.member-name{font-family:'Montserrat',sans-serif;font-weight:700;font-size:22px;letter-spacing:1px;text-transform:uppercase;margin-top:40px}
.member-bio{font-size:15px;line-height:1.3;color:var(--muted);margin-top:16px}
.member-shadow{width:160px;height:10px;margin:50px auto 0;border-radius:50%;background:radial-gradient(ellipse,rgba(0,0,0,.14),transparent 70%)}
.btn-outline-dark{border:2px solid var(--ink);color:var(--ink);font-size:12px;padding:16px 40px}

/* Service bands */
.service{position:relative;color:var(--white)}
.service-web{background:var(--orange);height:542px}
.service-content{background:var(--blue);height:543px}
.service-graphic{background:var(--yellow);height:539px}
.service-coach{background:var(--teal);height:536px}
.service-copy{position:absolute;top:40px;width:500px}
.service-copy.left{left:108px}
.service-copy.right{right:60px;text-align:right}
.service-title{font-family:'Montserrat',sans-serif;font-weight:800;font-size:40px;text-transform:uppercase;letter-spacing:.5px}
.service-copy p{font-family:'Montserrat',sans-serif;font-weight:600;font-size:14.5px;line-height:2;margin-top:22px}
.service-copy .btn{margin-top:30px;font-size:13px;padding:16px 54px}
.service-web .btn-solid{color:var(--orange)}
.service-content .btn-solid{color:var(--blue)}
.service-graphic .btn-solid{color:var(--yellow)}
.service-coach .btn-solid{color:var(--teal)}
.service-art{position:absolute;border-radius:24px}
.service-web .service-art{left:600px;top:50px;width:560px;height:440px;background:radial-gradient(circle at 50% 55%,#fbe3d8,#f59a7a 55%,var(--orange) 75%)}
.service-content .service-art{left:20px;top:30px;width:560px;height:480px;background:radial-gradient(circle at 45% 55%,#e8f4fb,#7fcbed 55%,var(--blue) 78%)}
.service-graphic .service-art{left:660px;top:40px;width:500px;height:460px;background:radial-gradient(circle at 50% 55%,#f3f1ea,#e0c470 55%,var(--yellow) 78%)}
.service-coach .service-art{left:20px;top:20px;width:520px;height:490px;background:radial-gradient(circle at 40% 50%,#e9f1f5,#7aa9c9 50%,var(--teal) 78%)}

/* Call to action */
.cta{position:relative;height:536px;color:var(--white);text-align:center}
.cta-bg{position:absolute;inset:0;background:linear-gradient(135deg,var(--cta-a),var(--cta-b) 55%,#3c3c3e)}
.cta-inner{position:relative;padding-top:106px}
.cta-title{font-family:'Montserrat',sans-serif;font-weight:800;font-size:42px;letter-spacing:4px;text-transform:uppercase}
.cta-sub{font-family:'Montserrat',sans-serif;font-weight:600;font-size:18px;letter-spacing:1px;line-height:1.45;margin-top:40px}
.cta .btn-row{margin-top:64px}

/* Footer */
.site-footer{background:var(--footer);height:378px;padding:50px 0 0 108px;color:var(--footer-text);position:relative}
.footer-cols{display:flex}
.footer-col{width:254px}
.footer-col h4{font-family:'Montserrat',sans-serif;font-weight:700;font-size:17px;letter-spacing:1.5px;color:var(--white);text-transform:uppercase}
.footer-col ul{list-style:none;margin-top:46px}
.footer-col li{font-size:17px;margin-bottom:22px}
.footer-brand{position:absolute;left:870px;top:226px}
.footer-brand .brand-name{font-size:22px;color:var(--white)}
.footer-brand .brand-tag{color:var(--footer-text);font-size:8px}
.footer-bar{background:var(--footer-bar);height:89px;display:flex;align-items:center;justify-content:space-between;padding:0 108px;color:var(--footer-text);font-size:17px;border-top:1px solid #3a3d43}
.footer-bar .legal a{color:#6fa6dc;text-decoration:underline}
.social{display:flex;gap:10px}
.social span{width:32px;height:32px;border-radius:50%;background:#6a6d73}
</style>
</head>
<body>

<header class="site-nav">
  <div class="brand">
    <span class="brand-name">rising harbour</span>
    <span class="brand-tag">PLAN | BUILD | GROW ONLINE</span>
  </div>
  <nav class="nav-links">
    <a href="#">About</a>
    <a href="#">How We Work</a>
    <a href="#">Learn</a>
    <a href="#">Shop</a>
    <a href="#">Contact</a>
    <a href="#" class="nav-signin">Sign in</a>
  </nav>
</header>

<section class="hero">
  <div class="hero-bg" role="img" aria-label="Blue-tinted photo of people working on laptops in a bright office"></div>
  <div class="hero-inner">
    <h1 class="hero-title">Want an online presence<br>for your<br>small business?</h1>
    <p class="hero-sub">Give your business the exposure it deserves! Get started by ordering services directly from the shop or by shooting us an email.</p>
    <div class="btn-row">
      <a href="#" class="btn btn-ghost">Shop</a>
      <a href="#" class="btn btn-solid">Contact</a>
    </div>
  </div>
</section>

<section class="experts">
  <h2 class="section-title">Our experts are there to help you</h2>
  <p class="experts-intro">Lorem ipsum dolor sit amet, consectetur adipiscing elit. Morbi auctor ut ligula sed fermentum.<br>Vestibulum elementum ultricies dui, eu placerat felis mattis.</p>
  <div class="team">
    <div class="member" style="left:237px;top:52px;width:260px">
      <div class="member-photo" role="img" aria-label="Portrait photo of Lena Marrow" style="width:250px;height:250px;background:radial-gradient(circle,#cfcfcf,#7d7d7d)"></div>
      <h3 class="member-name" style="margin-top:60px">Lena Marrow</h3>
      <p class="member-bio">Aenean tempor justo vitae orci iaculis rutrum. Vivamus porttitor augue nisi, ac molestie eros maximus sit amet.</p>
      <div class="member-shadow"></div>
    </div>
    <div class="member" style="left:602px;width:330px">
      <div class="member-photo" role="img" aria-label="Portrait photo of Owen Talbrook on a light teal circle" style="width:350px;height:350px;background:radial-gradient(circle,#f1f8f9,#cde9ec 70%,#b9dfe3)"></div>
      <h3 class="member-name">Owen Talbrook</h3>
      <p class="member-bio" style="font-size:17px">Aenean tempor justo vitae orci iaculis rutrum. Vivamus porttitor augue nisi, ac molestie eros maximus sit amet.</p>
      <div class="member-shadow" style="width:200px;margin-top:40px"></div>
    </div>
    <div class="member" style="left:960px;top:52px;width:260px">
      <div class="member-photo" role="img" aria-label="Portrait photo of Ray Fennick" style="width:250px;height:250px;background:radial-gradient(circle,#bdbdbd,#555)"></div>
      <h3 class="member-name" style="margin-top:60px">Ray Fennick</h3>
      <p class="member-bio">Aenean tempor justo vitae orci iaculis rutrum. Vivamus porttitor augue nisi, ac molestie eros maximus sit amet.</p>
      <div class="member-shadow"></div>
    </div>
    <a href="#" class="btn btn-outline-dark" style="position:absolute;left:50%;top:636px;transform:translateX(-50%)">See more about us</a>
  </div>
</section>

<section class="service service-web">
  <div class="service-copy left">
    <h2 class="service-title">Web Design</h2>
    <p>Let's be honest. Your website is the face of your business in the modern world.</p>
    <p>When done well, it can communicate personality, expertise, and high-quality of service. And done poorly?</p>
    <p>Let's just say it'll do more harm than good. From total reconstructive surgery to a simple makeover, we'll help make sure the face of your business is a welcoming one.</p>
    <a href="#" class="btn btn-solid">Learn more</a>
  </div>
  <div class="service-art" role="img" aria-label="Illustration of a desktop monitor surrounded by web and social icons"></div>
</section>

<section class="service service-content">
  <div class="service-art" role="img" aria-label="Illustration of a light bulb, gear, target, laptop and envelope"></div>
  <div class="service-copy right">
    <h2 class="service-title">Content Marketing</h2>
    <p>Content Marketing is to the 21st century what traditional advertising was to the '60s.</p>
    <p>Thanks to the power of the internet, so many businesses have never had such access to their customers. And so many businesses have never been so lost on how to use it.</p>
    <p>Our content marketing services create valuable content your audience pays attention to, giving your business the credibility to turn them into lifelong customers.</p>
    <a href="#" class="btn btn-solid">Learn more</a>
  </div>
</section>

<section class="service service-graphic">
  <div class="service-copy left">
    <h2 class="service-title">Graphic Design</h2>
    <p>Creating a consistent and eye-catching brand for your business is one of the best ways to draw in customers on the web. And nothing builds a brand like top-notch graphic design.</p>
    <p>From display ads and social media graphics to stickers and blog headers, our graphic design service has got you covered.</p>
    <p>Just let us know what you're looking for and we'll find a way to make it come to life.</p>
    <a href="#" class="btn btn-solid">Learn more</a>
  </div>
  <div class="service-art" role="img" aria-label="Illustration of a laptop, drawing tablet, colour swatches and sketchbook"></div>
</section>

<section class="service service-coach">
  <div class="service-art" role="img" aria-label="Illustration of a presenter at an easel teaching a seated group"></div>
  <div class="service-copy right">
    <h2 class="service-title">Coaching</h2>
    <p>Taking your small business to the next level can be a tricky process. Marketing jargon, confusing tools, and literally millions of resources can make expanding seem like an impossible task.</p>
    <p>But luckily, you don't have to do it alone.</p>
    <p>Our coaching services help you untangle the mess so you can get the most out of your marketing efforts and create an online presence you'll be proud of.</p>
    <a href="#" class="btn btn-solid">Learn more</a>
  </div>
</section>

<section class="cta">
  <div class="cta-bg" role="img" aria-label="Dark grey photo of a person relaxing with feet up at a desk"></div>
  <div class="cta-inner">
    <h2 class="cta-title">We've got your back</h2>
    <p class="cta-sub">We'll help you move your business into the digital world,<br>so you can get back to doing what you love.</p>
    <div class="btn-row">
      <a href="#" class="btn btn-solid">Get started</a>
      <a href="#" class="btn btn-ghost">Learn more</a>
    </div>
  </div>
</section>

<footer>
  <div class="site-footer">
    <div class="footer-cols">
      <div class="footer-col"><h4>Product</h4><ul><li>Features</li><li>Services</li><li>Products</li><li>Solutions</li></ul></div>
      <div class="footer-col"><h4>Resources</h4><ul><li>Harbour Shop</li><li>Inspiration Center</li><li>Success Stories</li><li>Developer Docs</li></ul></div>
      <div class="footer-col"><h4>Company</h4><ul><li>About</li><li>Careers</li><li>Press</li><li>Contact</li></ul></div>
      <div class="footer-col"><h4>Support</h4><ul><li>Support Center</li><li>Community</li></ul></div>
    </div>
    <div class="footer-brand brand">
      <span class="brand-name">rising harbour</span>
      <span class="brand-tag">PLAN | BUILD | GROW ONLINE</span>
    </div>
  </div>
  <div class="footer-bar">
    <span class="legal">© Rising Harbour, Inc. <a href="#">Terms</a> <a href="#">Privacy Policy</a></span>
    <div class="social"><span></span><span></span><span></span><span></span><span></span></div>
  </div>
</footer>

</body>
</html>
```